Flyer-Design für Sabine Wellrath Coaching für Führungskräfte
Zielgruppe
Coaching für Führungskräfte, Seminare für Führungskräfte.
Zielgruppe: Führungskräfte, Unternehmer, Geschäftsführer, Vorstände
Aufgabenstellung
Mein Logo soll beibehalten werden. Es soll ein vierseitiger Flyer sein, der meine Leistungen beschreibt. Es soll sehr modern sein (Stichwort: digital leadership) und seriös. Möglichst nicht das übliche Format, aber nicht zu groß.
Der Text soll weitgehend aus meiner Homepage (www.coaching-wellrath-beispiel.de) übernommen werden, aber es sollen auch zusätzlich Seminare aufgeführt werden.
Bis auf das Logo müssen die angehängten Dateien nicht unbedingt verwendet werden.

```html
<!DOCTYPE html>
<html lang="de">
<head>
<meta charset="utf-8">
<title>Flyer – Sabine Wellrath Coaching</title>
<link href="https://fonts.googleapis.com/css2?family=Source+Sans+3:wght@300;400;500;600;700&display=swap" rel="stylesheet">
<style>
  :root {
    --backdrop: #808080;
    --paper: #ffffff;
    --magenta: #c90768;
    --navy: #0d3d6b;
    --ink: #1f1f1f;
    --sky-light: #dfe6ee;
    --sky-mid: #9fb4c9;
    --rock: #0f4271;
    --portrait-light: #c9d6e2;
    --portrait-dark: #2f5173;
    --logo-tile: #b7d2ea;
  }
  * { margin: 0; padding: 0; box-sizing: border-box; }
  html, body { width: 1200px; height: 1200px; overflow: hidden; }
  body {
    background: var(--backdrop);
    font-family: "Source Sans 3", "Source Sans Pro", sans-serif;
    position: relative;
  }
  .spread {
    position: absolute; left: 15px; top: 184px;
    width: 1170px; height: 831px;
    background: var(--paper);
  }
  .abs { position: absolute; }
  .portrait {
    left: 19px; top: 141px; width: 261px; height: 175px;
    background: linear-gradient(100deg, var(--portrait-dark) 0%, var(--portrait-light) 45%, var(--sky-light) 100%);
  }
  .section-title {
    left: 19px; top: 335px;
    font-size: 22px; font-weight: 400; color: var(--magenta); letter-spacing: .2px;
  }
  .copy {
    font-size: 12.3px; line-height: 19.6px; color: var(--ink); font-weight: 400;
    letter-spacing: -0.1px;
  }
  .copy p + p, .copy p + ul, .copy ul + p { margin-top: 19.6px; }
  .copy ul { list-style: none; }
  .copy li { padding-left: 12px; position: relative; }
  .copy li::before { content: "•"; position: absolute; left: 0; }
  .copy .accent { color: var(--navy); font-weight: 500; }
  .copy .contact { color: var(--magenta); font-weight: 500; }
  .col-left { left: 19px; top: 389px; width: 258px; }
  .col-mid { left: 300px; top: 136px; width: 256px; }
  .cover-band {
    left: 605px; top: 20px; width: 546px; height: 281px;
    background: var(--magenta);
  }
  .cover-title {
    left: 632px; top: 146px;
    font-size: 32px; color: var(--paper); font-weight: 300; letter-spacing: .4px;
  }
  .cover-title strong { font-weight: 700; }
  .cover-photo {
    left: 605px; top: 301px; width: 546px; height: 358px;
    background: linear-gradient(180deg, var(--sky-mid) 0%, var(--sky-light) 45%, var(--sky-mid) 68%, var(--rock) 72%, var(--rock) 100%);
  }
  .brand { display: flex; flex-direction: column; gap: 9px; }
  .brand-mark { width: 50px; height: 50px; background: var(--logo-tile); }
  .brand-name {
    font-size: 14.5px; line-height: 16.5px; color: var(--navy); font-weight: 500;
  }
  .brand-left { left: 206px; top: 703px; }
  .brand-right { left: 791px; top: 703px; }
</style>
</head>
<body>
  <main class="spread">
    <div class="abs portrait" role="img" aria-label="Porträtfoto der Coachin in Blautönen"></div>
    <h2 class="abs section-title">Meine Erfahrungen</h2>

    <div class="abs copy col-left">
      <p>mehr als 20 Jahre in Führungspositionen in einem internationalen Unternehmen</p>
      <ul>
        <li>Personalauswahl, Coaching und Training</li>
        <li>Mediation (Mitglied im Fachverband Mediation Nord)</li>
        <li>Psychotherapie (HPG)</li>
      </ul>
      <p class="accent">Es ist meine Berufung, Menschen in ihrem Arbeitsumfeld mit Wertschätzung auf dem Weg zu Zufriedenheit und Erfolg zu begleiten. Diese Begegnungen haben mich reich an Erfahrung gemacht. Davon können Sie profitieren.</p>
    </div>

    <div class="abs copy col-mid">
      <p>Coaching- und Mediationsweiterbildung beim Hochschulnetzwerk Nordstadt</p>
      <p>Univ. Zertifizierung als Mediator und Coach am Institut für Dialogische Kommunikation und Vielfalts-Kompetenz (IDK) an der Akademie für moderne Pädagogik, Psychologie und Wirtschaft (APW) Beispielstadt http://www.apw-beispiel.org/institut/idk</p>
      <p>Wenn Sie mehr erfahren möchten, empfehle ich ein Interview, welches durch www.coach-interviews-beispiel.de mit mir geführt wurde.</p>
      <p class="accent">Bei Fragen oder Interesse an einer Beratung schreiben Sie mir per Mail oder rufen Sie mich direkt an unter 0151 48217736. Gerne können wir Termine vereinbaren, ich freue mich auf Sie!</p>
      <p class="contact">Sabine Wellrath<br>Coaching für Führungskräfte<br>Am Lindenweg 7<br>40210 Musterstadt</p>
      <p class="contact">Mobil: 0151 48217736<br>E-Mail: anfrage@coaching-wellrath-beispiel.de</p>
    </div>

    <div class="abs cover-band"></div>
    <h1 class="abs cover-title"><strong>Coaching</strong> Sabine Wellrath</h1>
    <div class="abs cover-photo" role="img" aria-label="Silhouetten von Bergsteigern, die sich am Seil auf einen Felsgipfel helfen, vor hellem Himmel"></div>

    <div class="abs brand brand-left">
      <span class="brand-mark"></span>
      <span class="brand-name">Sabine Wellrath<br>Coaching für Führungskräfte</span>
    </div>
    <div class="abs brand brand-right">
      <span class="brand-mark"></span>
      <span class="brand-name">Sabine Wellrath<br>Coaching für Führungskräfte</span>
    </div>
  </main>
</body>
</html>
```